Delworth Consulting Updated Web design

We need to update our website, reconfigure some pages, have the availability for people to register for courses and integrate with our on-line store. It must be something were a novice (like myself) can update classes as they are changed almost daily. We offer training to Police, Fire and 911 Operators so it should be themed as such. See current site at delworthconsulting.example It should have a clear POLICE, FIRE, 911 DISPATCH on home screen to bring visitors to their area and we will need subcategory of pages from there. See uploaded site map for details. I will need guidance on how to get your design up and live, small operation and none of us are tech savvy.

Target Market(s)

Police Officers and Departments, Fire Departments and Dispatch 911

Coding

Coded - Design and coding required

Number of Pages Required

5+ page

Requirements
Must have
• See uploaded word document with site map

```html
<!DOCTYPE html>
<html lang="en">
<head>
<meta charset="utf-8">
<title>Delworth Consulting, LLC</title>
<link rel="stylesheet" href="https://fonts.googleapis.com/css2?family=Rajdhani:wght@500;600;700&family=Raleway:wght@400;500;600;700&display=swap">
<style>
:root{
  --yellow:#f4c21a;
  --blue:#1f3f9b;
  --navy:#263248;
  --ink:#222222;
  --text:#444444;
  --muted:#777777;
  --light:#f4f5f8;
  --footer:#1e2126;
  --white:#ffffff;
}
*{box-sizing:border-box;margin:0;padding:0}
html,body{width:1200px;height:3702px;overflow:hidden}
body{position:relative;font-family:"Raleway",sans-serif;color:var(--text);background:var(--white)}
.display{font-family:"Rajdhani",sans-serif;font-weight:700;letter-spacing:.5px;color:var(--ink)}

/* header */
.site-header{position:absolute;left:0;top:0;width:1200px;height:83px;background:var(--white);z-index:3}
.top-rule{position:absolute;left:0;top:0;width:700px;height:5px;background:var(--yellow)}
.contact-bar{position:absolute;right:0;top:0;width:500px;height:44px;background:var(--yellow);clip-path:polygon(40px 0,100% 0,100% 100%,90px 100%)}
.contact-icon{position:absolute;left:775px;top:8px;width:28px;height:28px;border-radius:50%;background:var(--white)}
.contact-phone{position:absolute;left:812px;top:2px;font-size:17px;font-weight:700;color:var(--white)}
.contact-mail{position:absolute;left:812px;top:24px;font-size:11px;color:var(--white)}
.account-links{position:absolute;left:1001px;top:14px;font-size:11px;color:var(--white)}
.brand{position:absolute;left:116px;top:10px;display:flex;align-items:center;gap:8px}
.brand-mark{width:22px;height:22px;border-radius:50%;background:var(--navy)}
.brand-name{font-family:"Rajdhani",sans-serif;font-weight:700;font-size:18px;color:var(--navy)}
.main-nav{position:absolute;left:544px;top:58px;display:flex;font-family:"Rajdhani",sans-serif;font-weight:600;font-size:12px;color:var(--ink)}
.main-nav span{margin-right:40px}
.main-nav span:last-child{margin-right:0}
.main-nav .active{color:var(--yellow)}

/* hero */
.hero{position:absolute;left:0;top:83px;width:1200px;height:532px;background:linear-gradient(100deg,#1d2535 0%,#2a3446 45%,#55627a 70%,#2b3140 100%)}
.hero-mark{position:absolute;left:114px;top:224px;width:60px;height:60px;border-radius:50%;background:var(--yellow);opacity:.9}
.hero-kicker{position:absolute;left:113px;top:319px;font-family:"Rajdhani",sans-serif;font-weight:600;font-size:24px;letter-spacing:3px;color:var(--white)}
.hero-title{position:absolute;left:112px;top:345px;font-family:"Rajdhani",sans-serif;font-weight:700;font-size:48px;color:var(--white);letter-spacing:1px}
.hero-title em{font-style:normal;color:var(--yellow)}
.hero-tag{position:absolute;left:111px;top:409px;font-size:13px;color:var(--white)}
.btn{position:absolute;display:flex;align-items:center;justify-content:center;font-size:12px;font-weight:700}
.btn-yellow{background:var(--yellow);color:var(--ink)}
.btn-white{background:var(--white);color:var(--ink)}
.btn-blue{background:var(--blue);color:var(--white);font-size:11px}
.slider-dots{position:absolute;left:1058px;top:572px;display:flex;gap:4px}
.slider-dots i{width:7px;height:7px;background:var(--white)}
.slider-dots i.on{background:var(--yellow)}

/* about */
.about-photo{position:absolute;left:112px;top:690px;width:475px;height:421px;background:linear-gradient(135deg,#d7d7d7,#8a8a8a 55%,#3a3a3a)}
.eyebrow{position:absolute;font-size:16px;color:var(--yellow);font-weight:500}
.section-title{position:absolute;font-family:"Rajdhani",sans-serif;font-weight:700;font-size:37px;color:var(--ink);letter-spacing:1px}
.body-copy{position:absolute;font-size:13px;line-height:22px;color:var(--text)}

/* what we do */
.services-band{position:absolute;left:0;top:1185px;width:1200px;height:487px;background:var(--navy)}
.band-title{position:absolute;left:0;top:1255px;width:1200px;text-align:center;font-family:"Rajdhani",sans-serif;font-weight:700;font-size:38px;color:var(--white);letter-spacing:1px}
.shield{position:absolute;top:1315px;width:186px;height:225px}
.shield-label{position:absolute;top:1556px;width:240px;text-align:center;font-family:"Rajdhani",sans-serif;font-weight:600;font-size:18px;line-height:24px;letter-spacing:1.5px;color:var(--white)}

/* cards */
.card-photo{position:absolute;width:475px;height:306px}
.card-eyebrow{position:absolute;font-size:15px;color:var(--yellow);font-weight:500}
.card-title{position:absolute;font-family:"Rajdhani",sans-serif;font-weight:700;font-size:26px;color:var(--ink);letter-spacing:.5px}
.card-copy{position:absolute;width:430px;font-size:12.5px;line-height:19px;color:var(--text)}

/* testimonial */
.testimonial{position:absolute;left:0;top:2882px;width:1200px;height:447px;background:var(--light)}
.center{position:absolute;left:0;width:1200px;text-align:center}
.avatar{position:absolute;left:559px;top:3020px;width:82px;height:82px;border-radius:50%;background:radial-gradient(circle,#b8bcc4,#4c525c)}
.quote{position:absolute;left:195px;top:3123px;width:810px;text-align:center;font-size:14px;line-height:20px;color:var(--text)}
.t-dots{position:absolute;left:586px;top:3268px;display:flex;gap:4px}
.t-dots i{width:7px;height:7px;background:var(--ink)}
.t-dots i.on{background:var(--yellow)}

/* footer */
.site-footer{position:absolute;left:0;top:3329px;width:1200px;height:373px;background:var(--footer)}
.f-head{position:absolute;top:3382px;font-family:"Rajdhani",sans-serif;font-weight:600;font-size:16px;color:var(--white);letter-spacing:.5px}
.f-list{position:absolute;top:3420px;font-size:11px;line-height:26px;color:#8a8d93;list-style:none}
.f-item{position:absolute;left:674px;font-size:11px;line-height:15px;color:#8a8d93}
.f-icon{position:absolute;left:654px}
.footer-brand{position:absolute;left:985px;top:3450px;display:flex;align-items:center;gap:8px}
.footer-brand .brand-mark{background:var(--yellow)}
.footer-brand .brand-name{color:var(--white);font-size:17px}
.social{position:absolute;top:3591px;left:545px;display:flex;gap:8px}
.social i{width:30px;height:30px;border-radius:50%}
.copyright{position:absolute;left:0;top:3637px;width:1200px;text-align:center;font-size:10px;color:#8a8d93}
.copyright b{font-weight:400;color:var(--yellow)}
</style>
</head>
<body>

<header class="site-header">
  <div class="top-rule"></div>
  <div class="contact-bar"></div>
  <div class="contact-icon">
    <svg width="28" height="28" viewBox="0 0 28 28"><path d="M8 14 L20 8 L16 20 L14 15 Z" fill="#263248"/></svg>
  </div>
  <div class="contact-phone">555.014.2290</div>
  <div class="contact-mail">info@delworthconsulting.example</div>
  <div class="account-links">Login &nbsp;|&nbsp; Register</div>
  <div class="brand"><span class="brand-mark"></span><span class="brand-name">Delworth Consulting</span></div>
  <nav class="main-nav">
    <span class="active">HOME</span><span>POLICE</span><span>FIRE</span><span>911 DISPATCH</span><span>UPCOMING COURSE LIST</span><span>ABOUT US</span>
  </nav>
</header>

<section class="hero" role="img" aria-label="Riot police officer in helmet and visor during a crowd deployment"></section>
<div class="hero-mark"></div>
<div class="hero-kicker">DELWORTH</div>
<h1 class="hero-title">CONSULTING, <em>LLC</em></h1>
<p class="hero-tag">PUBLIC SAFETY PROMOTIONS, TRAINING, SELECTION &amp; MORE</p>
<div class="btn btn-yellow" style="left:113px;top:437px;width:219px;height:38px">VISIT OUR ON-LINE STORE NOW !</div>
<div class="btn btn-white" style="left:341px;top:437px;width:259px;height:38px">CHECK UPCOMING COURSE SCHEDULE</div>
<div class="slider-dots"><i class="on"></i><i></i><i></i></div>

<section>
  <div class="about-photo" role="img" aria-label="Black and white photo of a police officer in dress uniform at an official event"></div>
  <div class="eyebrow" style="left:614px;top:762px">ABOUT</div>
  <h2 class="section-title" style="left:614px;top:785px">DELWORTH CONSULTING</h2>
  <p class="body-copy" style="left:613px;top:847px;width:478px">Delworth Consulting, LLC was founded by Martin Delworth. Martin is a Massachusetts licensed attorney and a police manager with more than 20 years of experience.&nbsp;&nbsp; Martin was promoted to sergeant within 3 years and to lieutenant within 4 years of his law enforcement career.&nbsp; Soon thereafter, Martin began helping co-workers and friends in law enforcement prepare for promotional exams informally.</p>
  <div class="btn btn-blue" style="left:613px;top:997px;width:113px;height:39px">READ MORE</div>
</section>

<section class="services-band"></section>
<h2 class="band-title">WHAT WE DO</h2>
<svg class="shield" style="left:131px" viewBox="0 0 186 225" role="img" aria-label="Police officer in sunglasses at night">
  <defs><linearGradient id="g1" x1="0" y1="0" x2="0" y2="1"><stop offset="0" stop-color="#5a4a7a"/><stop offset="1" stop-color="#1a1f3a"/></linearGradient></defs>
  <path d="M93 4 Q130 30 183 30 L183 120 Q183 190 93 222 Q3 190 3 120 L3 30 Q56 30 93 4 Z" fill="url(#g1)" stroke="#f4c21a" stroke-width="3"/>
</svg>
<svg class="shield" style="left:382px" viewBox="0 0 186 225" role="img" aria-label="Firefighter in turnout gear">
  <defs><linearGradient id="g2" x1="0" y1="0" x2="0" y2="1"><stop offset="0" stop-color="#8a5a3a"/><stop offset="1" stop-color="#2a2420"/></linearGradient></defs>
  <path d="M93 4 Q130 30 183 30 L183 120 Q183 190 93 222 Q3 190 3 120 L3 30 Q56 30 93 4 Z" fill="url(#g2)" stroke="#ffffff" stroke-width="3"/>
</svg>
<svg class="shield" style="left:633px" viewBox="0 0 186 225" role="img" aria-label="Two officers studying at a desk">
  <defs><linearGradient id="g3" x1="0" y1="0" x2="0" y2="1"><stop offset="0" stop-color="#e6e2da"/><stop offset="1" stop-color="#4a4e5a"/></linearGradient></defs>
  <path d="M93 4 Q130 30 183 30 L183 120 Q183 190 93 222 Q3 190 3 120 L3 30 Q56 30 93 4 Z" fill="url(#g3)" stroke="#f4c21a" stroke-width="3"/>
</svg>
<svg class="shield" style="left:882px" viewBox="0 0 186 225" role="img" aria-label="Officer training at a firing range">
  <defs><linearGradient id="g4" x1="0" y1="0" x2="0" y2="1"><stop offset="0" stop-color="#5f8a7a"/><stop offset=".5" stop-color="#d8dcd8"/><stop offset="1" stop-color="#2a2a2a"/></linearGradient></defs>
  <path d="M93 4 Q130 30 183 30 L183 120 Q183 190 93 222 Q3 190 3 120 L3 30 Q56 30 93 4 Z" fill="url(#g4)" stroke="#ffffff" stroke-width="3"/>
</svg>
<div class="shield-label" style="left:104px">BAYSIDE<br>POLICE PRODUCTS</div>
<div class="shield-label" style="left:355px">FIRE PROMOTION<br>&amp; ENTRANCE EXAMS</div>
<div class="shield-label" style="left:606px">POLICE PROMOTION<br>EXAM PREP</div>
<div class="shield-label" style="left:855px">POLICE TRAINING &amp;<br>REFERENCES</div>

<section>
  <div class="card-photo" style="left:112px;top:1748px;background:linear-gradient(160deg,#6b7e95,#2a3444 60%,#171c24)" role="img" aria-label="Line of officers in tactical gear"></div>
  <div class="card-eyebrow" style="left:112px;top:2083px">POLICE</div>
  <h3 class="card-title" style="left:112px;top:2101px">PROMOTIONAL PREPARATION</h3>
  <p class="card-copy" style="left:112px;top:2141px">We have quickly become the leader in Police Promotional Preparation in Massachusetts.</p>
  <div class="btn btn-blue" style="left:112px;top:2198px;width:114px;height:40px">READ MORE</div>

  <div class="card-photo" style="left:613px;top:1783px;background:linear-gradient(150deg,#9a9ea8,#dbe85a 45%,#2a2e36)" role="img" aria-label="Public safety vest with reflective lettering"></div>
  <div class="card-eyebrow" style="left:613px;top:2118px">PUBLIC SAFETY</div>
  <h3 class="card-title" style="left:613px;top:2136px">EMPLOYMENT PREPARATION</h3>
  <p class="card-copy" style="left:613px;top:2176px">Exam preparation, interviewing &amp; assessment centers, career path and job search.</p>
  <div class="btn btn-blue" style="left:613px;top:2233px;width:114px;height:40px">READ MORE</div>

  <div class="card-photo" style="left:112px;top:2281px;background:linear-gradient(120deg,#a88a78,#b8242a 45%,#5a8a4a 75%,#c8c8c0)" role="img" aria-label="Hand holding a phone showing an emergency call"></div>
  <div class="card-eyebrow" style="left:112px;top:2616px">911</div>
  <h3 class="card-title" style="left:112px;top:2634px">TRAINING COURSES</h3>
  <p class="card-copy" style="left:112px;top:2674px">Advanced &amp; Specialized legal training for State, Municipal and Campus Police. Custom tailor training to the needs.</p>
  <div class="btn btn-blue" style="left:112px;top:2731px;width:114px;height:40px">READ MORE</div>

  <div class="card-photo" style="left:613px;top:2316px;background:linear-gradient(135deg,#7a5a44,#4a3426 50%,#2a1e16)" role="img" aria-label="People reviewing and signing a document at a wooden table"></div>
  <div class="card-eyebrow" style="left:613px;top:2651px">LAW ENFORCEMENT</div>
  <h3 class="card-title" style="left:613px;top:2669px">AGENCY SERVICES</h3>
  <p class="card-copy" style="left:613px;top:2709px">Training, Entrance and Promotional Exam creation and administration, Assessment Centers and selection assistance.</p>
  <div class="btn btn-blue" style="left:613px;top:2766px;width:114px;height:40px">READ MORE</div>
</section>

<section class="testimonial"></section>
<div class="center display" style="top:2933px;font-size:20px;font-weight:600;letter-spacing:1.5px">TESTIMONIAL</div>
<h2 class="center display" style="top:2960px;font-size:38px;letter-spacing:1.5px">FROM PREVIOUS CLIENTS</h2>
<div class="avatar" role="img" aria-label="Portrait of a police chief in uniform cap"></div>
<p class="quote">Hey Martin, I just wanted to let you know that I was lucky enough to get promoted to Chief last week here in XXXXX. Part of the reason I was able to do that was because of you. I am not sending this for any other reason but to say thanks and if there is ever anything I can do to help you in the future please feel free to call.</p>
<div class="center" style="top:3214px;font-size:14px;font-weight:600;color:var(--ink)">Chief Daniel R. Fenwick</div>
<div class="center" style="top:3233px;font-size:10px;color:var(--muted)">Harborview Police Department</div>
<div class="t-dots"><i class="on"></i><i></i><i></i></div>

<footer class="site-footer"></footer>
<div class="f-head" style="left:112px">SITEMAP</div>
<ul class="f-list" style="left:112px"><li>Home</li><li>Police</li><li>Fire</li><li>911 Dispatch</li><li>Upcoming Course List</li><li>About Us</li></ul>
<div class="f-head" style="left:336px">POLICE</div>
<ul class="f-list" style="left:336px"><li>Police Promotional Preparation</li><li>Police Department</li><li>Police Entrance Exam Preparation</li><li>Upcoming courses</li></ul>
<div class="f-head" style="left:654px">CONTACT US</div>
<svg class="f-icon" style="top:3420px" width="12" height="14" viewBox="0 0 12 14"><path d="M6 0a5 5 0 0 1 5 5c0 4-5 9-5 9S1 9 1 5a5 5 0 0 1 5-5z" fill="#f4c21a"/><circle cx="6" cy="5" r="2" fill="#1e2126"/></svg>
<div class="f-item" style="top:3419px">Delworth Consulting, LLC P.O. Box<br>120, Millbrook, MA 01000</div>
<svg class="f-icon" style="top:3478px" width="12" height="14" viewBox="0 0 12 14"><path d="M2 1 L5 1 L6 4 L4 5 Q5 8 8 10 L9 8 L12 9 L12 12 Q6 13 2 7 Q0 4 2 1Z" fill="#f4c21a"/></svg>
<div class="f-item" style="top:3478px">555.014.2290</div>
<svg class="f-icon" style="top:3523px" width="13" height="10" viewBox="0 0 13 10"><rect width="13" height="10" fill="#f4c21a"/><path d="M0 0 L6.5 5 L13 0" stroke="#1e2126" fill="none"/></svg>
<div class="f-item" style="top:3521px">info@delworthconsulting.example</div>
<div class="footer-brand"><span class="brand-mark"></span><span class="brand-name">Delworth Consulting</span></div>
<div class="social" aria-label="Social links"><i style="background:#3b5998"></i><i style="background:#0e76a8"></i><i style="background:#cc1d1d"></i></div>
<div class="copyright">COPYRIGHT 2014. <b>DELWORTH CONSULTING</b>. ALL RIGHTS RESERVED.</div>

</body>
</html>
```